Insurance Postcard Design

We need a postcard design for my insurance agency serving a customers in the Silicon Valley area of Northern California. My agency focus is a specialized niche insuring Condominium and Townhouse Homeowner Associations (HOAs) which includes coverage for the HOA Buildings and Directors and Officers. (We do NOT insure autos, single family homes, life or health insurance so please do NOT use any of these themes)
The postcard color theme should be based on the blue with gold/orange stripe color scheme on my website www.kelmorbrant.com where you can also learn more about my specialized insurance business which might be helpful in designing the postcard.
My target customers are HOA Board Members also known as Directors and Officers.
The purpose of the card is to persuade Board Members to call or email me to 1. ask a question or request information, 2. request an HOA insurance evaluation 3. request a quote.
I would like the card Headline
to be: Attention HOA Board Members...
I have included an attached document with some compelling questions and responses that can be used on the postcard Side A and Side B. In designing the cards take into consideration... if postcards are delivered with the Address Side up as sorted by the postal carriers then is the Address Side of the card most likely to be seen first by the customer? If so, then should the question be listed on the Address Side and the answer be listed on the other side?
My attached document also includes a reward as an inducement to call or email me. This inducement should be prominent.
The card should also request a phone call or email multiple times.
I want to use color on both sides of the card.
I want to conduct a split test for results based on card size so please provide identical or nearly identical/comparable designs for both Quillmark Press Small Card Full Bleed size 6.12"x4.12" with Trim Size of 6"x4" and Quillmark Press Oversize Cards Full Bleed size 8.64"x5.59" with Trim Size of 8.52"x5.47".
Both the Small and Oversize card should use the same question and answer and should include the same inducement: a $10 Brewlark Card to everyone who calls or emails. No purchase required. Limited time offer.
After we get the card size results then future designs will include a split test using different inducements/special offers.
Other attached documents include my photo and photo of a Board Meeting that can be included in the design.
Let me know if the three docs: Personal photo, Board Meeting Photo and Headline & Questions did not load. Post a note and include your email and i'll forward any missing docs directly to you.
Reason: Want to provide sufficient time for designers to create postcard designs.
Per Gordon at Quillmark Press the correct card size designers should use is:
Small Card Full Bleed size 6.12" x 4.12" with Trim size 6" x 4"
Oversize Card Full Bleed size 8.64" x 5.59" with Trim size 8.52" x 5.47"
I want to conduct a split test using identical or very similar designs with two size cards to determine best response.
I just uploaded a fresh document dated 9.17.2014 listing Content to be used on the front and back side of the card. Ray Fenwick
Target Market(s)
Board Members aka Directors and Officers for condominium and townhouse homeowner associations. Typical age is 40 to 70. Majority are age 50+. Two out of three board members are women. Board members tend to be conservative. Majority of board members are white/anglo, but growing % is female Indian with lower % female Chinese.
Industry/Entity Type
Insurance
Requirements
Must have
- Try to match my website color scheme. www.kelmorbrant.com I believe shades of blue with orange stripe & buttons gets attention. My web Action buttons are orange.
Include my agency name, Lic. # 7K21364 and website www.kelmorbrant.com
on the card Office address should be included for Return Address: Gregory T. Fenwick Coverage Partners, LLC 3815 Larkfield Blvd. Ste. 207 San Jose, CA 95342
Nice to have
- If there is space on the post card an abbreviated version of the tag line in the orange stripe on my website www.kelmorbrant.com would be good to include: The Best Place to Learn About and Buy HOA Insurance
Should not have
- No insurance themes for auto, boat, motorcycle, single family home, life ins, health ins, financial services. I don't sell any of those products.

```html
<!DOCTYPE html>
<html lang="en">
<head>
<meta charset="utf-8">
<title>HOA Insurance Postcard</title>
<link rel="stylesheet" href="https://fonts.googleapis.com/css2?family=Roboto+Condensed:wght@300;400;700&family=Roboto:wght@400;700;900&display=swap">
<style>
:root{
  --stage:#d9dcdc;
  --navy:#161d48;
  --navy-deep:#0d1233;
  --blue:#1877e6;
  --orange:#f39a12;
  --orange-deep:#ef6a0c;
  --white:#ffffff;
  --ink:#111111;
  --rule:#555555;
}
*{margin:0;padding:0;box-sizing:border-box}
html,body{width:873px;height:1200px;overflow:hidden}
body{background:var(--stage);position:relative;font-family:"Roboto Condensed",Arial,sans-serif;color:var(--ink)}
.card{position:absolute;left:58px;width:765px;background:var(--white);overflow:hidden}
.card-front{top:58px;height:514px}
.card-back{top:620px;height:514px}

/* front */
.front-hero{position:absolute;left:0;top:0;width:765px;height:420px;background:radial-gradient(ellipse at 30% 40%,var(--navy) 0%,var(--navy-deep) 100%)}
.meeting-photo{position:absolute;left:275px;top:0;width:490px;height:405px;background:linear-gradient(160deg,#3b4a78 0%,#c9a978 45%,#e6c48a 60%,#4a5d8f 100%)}
.front-curve{position:absolute;left:0;top:385px;width:765px;height:60px}
.headline{position:absolute;left:32px;top:30px;color:var(--white);font-weight:700;text-transform:uppercase;line-height:.98}
.headline .big{display:block;font-size:76px;letter-spacing:1px}
.headline .mid{display:block;font-size:44px}
.accent{color:var(--orange)}
.lead{position:absolute;left:35px;top:248px;color:var(--white);font-weight:300;font-size:23px;line-height:1.2}
.lead b{font-weight:700}
.questions{position:absolute;left:32px;top:315px;font-weight:700;font-size:29px;text-transform:uppercase;line-height:1.17;color:var(--white)}
.front-contact{position:absolute;left:24px;top:424px;width:370px;text-align:center;color:var(--blue)}
.call-today{font-family:Roboto,Arial,sans-serif;font-weight:900;font-size:20px}
.contact-line{font-family:Roboto,Arial,sans-serif;font-weight:700;font-size:16px;margin-top:6px}
.address-line{font-family:Roboto,Arial,sans-serif;font-size:12.5px;margin-top:6px}
.sq{display:inline-block;width:9px;height:9px;background:var(--orange);margin:0 4px 1px 4px}
.agency-name{position:absolute;left:402px;top:420px;width:330px;text-align:center;color:var(--blue);font-size:34px;line-height:1.1;font-weight:400;transform:scaleY(1.05)}

/* back */
.back-banner{position:absolute;left:0;top:27px;width:402px;height:44px;background:var(--blue);color:var(--white);font-size:25px;font-weight:700;padding:6px 0 0 30px}
.offer-tab{position:absolute;left:368px;top:20px;width:234px;height:58px;background:linear-gradient(#f8891a,var(--orange-deep));border-radius:10px 10px 0 0;color:var(--white);text-align:center;font-family:Roboto,Arial,sans-serif;font-weight:900;line-height:1}
.offer-tab .amount{display:block;font-size:24px;padding-top:6px}
.offer-tab .card-word{display:block;font-size:17px;padding-top:3px}
.offer-body{position:absolute;left:402px;top:78px;width:200px;height:92px;background:linear-gradient(#ffffff,#d6d6d6);border-bottom:3px solid var(--orange);padding:5px 10px;font-size:12.6px;line-height:1.17}
.checklist{position:absolute;left:28px;top:80px;list-style:none;font-size:14px;line-height:1.2}
.checklist li{position:relative;padding-left:16px;margin-bottom:6px}
.checklist svg{position:absolute;left:0;top:3px}
.body-copy{position:absolute;left:28px;top:196px;font-size:14px;line-height:1.22;width:420px}
.body-copy p{margin-bottom:7px}
.what-we-do{position:absolute;left:28px;top:280px;font-size:20px;font-weight:700}
.audit-note{position:absolute;left:28px;top:310px;font-size:13px;font-weight:700;line-height:1.3}
.cta{position:absolute;left:28px;top:355px;color:var(--blue);font-size:21px;font-weight:700}
.call-free{position:absolute;left:28px;top:383px;color:var(--orange);font-size:29px;font-weight:700}
.back-links{position:absolute;left:24px;top:417px;color:var(--blue);font-family:Roboto,Arial,sans-serif;font-weight:700;font-size:13.5px}
.stamp-box{position:absolute;left:642px;top:34px;width:82px;height:93px;border:1px solid var(--rule)}
.return-note{position:absolute;left:624px;top:143px;width:120px;text-align:center;font-size:13px;font-weight:700;line-height:1.05}
.address-rule{position:absolute;left:477px;width:230px;border-top:1px solid var(--rule)}
</style>
</head>
<body>

<section class="card card-front" aria-label="Postcard front">
  <div class="front-hero"></div>
  <div class="meeting-photo" role="img" aria-label="Overhead photo of HOA board members meeting around a table with tablets and a laptop"></div>
  <svg class="front-curve" viewBox="0 0 765 60" preserveAspectRatio="none" aria-hidden="true">
    <path d="M0 0 H765 V20 Q382 -2 0 24 Z" fill="var(--navy-deep)"/>
    <path d="M0 24 Q382 -2 765 20 V28 Q382 8 0 32 Z" fill="var(--orange)"/>
    <path d="M0 32 Q382 8 765 28 V60 H0 Z" fill="var(--white)"/>
  </svg>
  <h1 class="headline">
    <span class="big">Attention</span>
    <span class="mid"><span class="accent">HOA</span> Board</span>
    <span class="mid">Members...</span>
  </h1>
  <p class="lead">As an <b>HOA</b> Board Member...<br>are your personal <b>assets exposed?</b></p>
  <p class="questions"><span class="accent">Are you covered?</span><br>Really? &nbsp;<span class="accent">How do you know?</span></p>
  <div class="front-contact">
    <div class="call-today">CALL TODAY!!</div>
    <div class="contact-line"><span class="sq"></span>877-555-0142 <span class="sq"></span>www.kelmorbrant.com</div>
    <div class="address-line">3815 Larkfield Blvd. #207 San Jose, CA 95342 <span class="sq"></span>Lic. # 7K21364</div>
  </div>
  <div class="agency-name">Gregory T. Fenwick<br>HOA Coverage Partners</div>
</section>

<section class="card card-back" aria-label="Postcard address side">
  <div class="back-banner">Attention HOA Board members...</div>
  <div class="offer-tab"><span class="amount">FREE $10</span><span class="card-word">BREWLARK CARD</span></div>
  <div class="offer-body">to everyone who makes an inquiry, requests an evaluation of their existing HOA insurance or who requests a quote. <b>No Purchase Required. Limited Time Offer.</b></div>

  <ul class="checklist">
    <li><svg width="12" height="12" viewBox="0 0 12 12" aria-hidden="true"><circle cx="6" cy="6" r="6" fill="var(--blue)"/><path d="M3 6.2l2 2 4-4.4" stroke="var(--orange)" stroke-width="1.8" fill="none"/></svg>When you get sued… will your Directors &amp; Officers policy<br>pay Legal Defense Costs?</li>
    <li><svg width="12" height="12" viewBox="0 0 12 12" aria-hidden="true"><circle cx="6" cy="6" r="6" fill="var(--blue)"/><path d="M3 6.2l2 2 4-4.4" stroke="var(--orange)" stroke-width="1.8" fill="none"/></svg>Are your personal assets exposed?</li>
    <li><svg width="12" height="12" viewBox="0 0 12 12" aria-hidden="true"><circle cx="6" cy="6" r="6" fill="var(--blue)"/><path d="M3 6.2l2 2 4-4.4" stroke="var(--orange)" stroke-width="1.8" fill="none"/></svg>Are current and <b>former</b> directors covered?</li>
    <li><svg width="12" height="12" viewBox="0 0 12 12" aria-hidden="true"><circle cx="6" cy="6" r="6" fill="var(--blue)"/><path d="M3 6.2l2 2 4-4.4" stroke="var(--orange)" stroke-width="1.8" fill="none"/></svg>Does your D&amp;O policy <b>exclude</b> Failure to Carry Sufficient Insurance?</li>
  </ul>

  <div class="body-copy">
    <p>Just because your D&amp;O policy is with a Big Name Company,<br>do you think they offer the best coverage? <b>Think again!</b></p>
    <p>Did you know… not all D&amp;O policies use the same definitions.<br>“Who Is An Insured” and “Wrongful Act” can significantly alter coverage.</p>
  </div>
  <h2 class="what-we-do">HOA insurance is what we do.</h2>
  <p class="audit-note">Based on our recent audits, over 40% of<br>HOA insurance coverage is out of compliance.</p>
  <p class="cta">Don’t blow it! &nbsp;Call or email today.</p>
  <p class="call-free">CALL FREE : 877-555-0142</p>
  <p class="back-links"><span class="sq"></span>info@kelmorbrant.com <span class="sq"></span>www.kelmorbrant.com</p>

  <div class="stamp-box" aria-label="Postage area"></div>
  <p class="return-note">Return Service<br>Requested</p>
  <div class="address-rule" style="top:242px"></div>
  <div class="address-rule" style="top:295px"></div>
  <div class="address-rule" style="top:344px"></div>
</section>

</body>
</html>
```